Brenford Automotive business card
Business card design for Brenford Automotive
Project: Brenford Automotive business card
Brenford Automotive business card - Automotive
Creative Brief
Simple
Wade Pelling
482 Kettle Lane Madison, WI 53790
brenautoco@mailnest.example
Hours: Mon-Thurs 7am-6pm
I want a simple road map on the back of the card, with the business location indicated with a star. The map should include Hwy 37, Hwy 21-29, Quarry Bend Rd, Larkfield Loop / Denholm St, Trobek Rd, Kettle Ln, and Corvell Rd.

```html
<!DOCTYPE html>
<html lang="en">
<head>
<meta charset="utf-8">
<title>Brenford Automotive business card</title>
<link rel="stylesheet" href="https://fonts.googleapis.com/css2?family=Saira:wght@400;500;600;700&display=swap">
<style>
  :root {
    --page-bg: #ece7de;
    --card-white: #ffffff;
    --card-grey: #e6e8ea;
    --blue-light: #3a9be0;
    --blue-mid: #1f78c4;
    --blue-dark: #15569a;
    --edge-black: #111418;
    --text-white: #ffffff;
    --brand-ink: #2d3238;
    --brand-dot: #1f78c4;
  }
  html, body {
    margin: 0;
    padding: 0;
    width: 1200px;
    height: 965px;
    overflow: hidden;
    background: var(--page-bg);
    font-family: "Saira", Arial, sans-serif;
  }
  .business-card {
    position: absolute;
    left: 100px;
    top: 197px;
    width: 1000px;
    height: 570px;
    border-radius: 34px;
    overflow: hidden;
    box-shadow: 0 8px 24px rgba(0, 0, 0, 0.18);
    background: linear-gradient(180deg, var(--card-white) 0%, var(--card-grey) 100%);
  }
  .card-shapes {
    position: absolute;
    inset: 0;
    width: 100%;
    height: 100%;
  }
  .contact-name {
    position: absolute;
    left: 34px;
    top: 38px;
    margin: 0;
    color: var(--text-white);
    font-size: 36px;
    font-weight: 600;
    letter-spacing: 0.3px;
  }
  .contact-address {
    position: absolute;
    left: 34px;
    top: 356px;
    margin: 0;
    color: var(--text-white);
    font-size: 24px;
    line-height: 32px;
    font-style: normal;
  }
  .contact-lines {
    position: absolute;
    left: 34px;
    top: 456px;
    margin: 0;
    padding: 0;
    list-style: none;
    color: var(--text-white);
    font-size: 21px;
    line-height: 36px;
    white-space: nowrap;
  }
  .contact-lines li {
    display: flex;
    align-items: center;
    gap: 10px;
  }
  .contact-lines svg {
    width: 20px;
    height: 20px;
    flex: none;
  }
  .brand-lockup {
    position: absolute;
    left: 500px;
    top: 262px;
    width: 470px;
    display: flex;
    align-items: center;
    justify-content: center;
    gap: 14px;
  }
  .brand-dot {
    width: 22px;
    height: 22px;
    border-radius: 50%;
    background: var(--brand-dot);
    flex: none;
  }
  .brand-name {
    margin: 0;
    color: var(--brand-ink);
    font-size: 36px;
    font-weight: 700;
    line-height: 1;
    white-space: nowrap;
  }
</style>
</head>
<body>
  <div class="business-card">
    <svg class="card-shapes" viewBox="0 0 1000 570" preserveAspectRatio="none" aria-hidden="true">
      <defs>
        <radialGradient id="panelBlue" cx="0.35" cy="0.45" r="0.75">
          <stop offset="0" stop-color="#3a9be0"/>
          <stop offset="0.6" stop-color="#1f78c4"/>
          <stop offset="1" stop-color="#15569a"/>
        </radialGradient>
      </defs>
      <path class="edge-band" d="M0 0 H492 C430 140 404 300 390 570 H0 Z" fill="var(--edge-black)"/>
      <path class="blue-panel" d="M0 0 H470 C410 140 386 300 374 570 H0 Z" fill="url(#panelBlue)"/>
    </svg>

    <h1 class="contact-name">Wade Pelling</h1>

    <address class="contact-address">482 Kettle Lane<br>Madison, WI 53790</address>

    <ul class="contact-lines">
      <li>
        <svg viewBox="0 0 24 24" aria-label="Phone"><path d="M6.6 10.8a15.1 15.1 0 0 0 6.6 6.6l2.2-2.2c.3-.3.7-.4 1-.2 1.1.4 2.3.6 3.6.6.6 0 1 .4 1 1V20c0 .6-.4 1-1 1A17 17 0 0 1 3 4c0-.6.4-1 1-1h3.5c.6 0 1 .4 1 1 0 1.3.2 2.5.6 3.6.1.3 0 .7-.2 1z" fill="var(--text-white)"/></svg>
        <span>(608) 555-0147</span>
      </li>
      <li>
        <svg viewBox="0 0 24 24" aria-label="Email"><circle cx="12" cy="12" r="4" fill="none" stroke="var(--text-white)" stroke-width="2.4"/><path d="M16 8v5.5a2.5 2.5 0 0 0 5 0V12a9 9 0 1 0-3.6 7.2" fill="none" stroke="var(--text-white)" stroke-width="2.4" stroke-linecap="round"/></svg>
        <span>brenautoco@mailnest.example</span>
      </li>
    </ul>

    <div class="brand-lockup">
      <span class="brand-dot"></span>
      <p class="brand-name">Brenford Automotive</p>
    </div>
  </div>
</body>
</html>
```